Project: Business Card and stationary
Use specific fonts
be Creative and professional bold
Modern
Marcus L. Fendrow
President/CEO
24731 Harlowe Rd Pinehollow, Tx 77590
mfendrow@tbpgrp.net
www.tbpbuildinggroup.net
Offical Company Name: Fendrow Trade Builders, Inc (TBP, Inc.) General Construction and Development Company Design/Build Services
Design/Build Contractor General Contractor Real Estate Development

```html
<!DOCTYPE html>
<html lang="en">
<head>
<meta charset="utf-8">
<title>Fendrow Trade Builders – Business Card</title>
<link rel="stylesheet" href="https://fonts.googleapis.com/css2?family=Roboto:ital,wght@0,400;0,700;0,900;1,400&family=Roboto+Slab:wght@700&display=swap">
<style>
  :root {
    --stage: #2b2b2c;
    --maroon: #5a1512;
    --maroon-deep: #4a100e;
    --paper: #ffffff;
    --ink: #3a3a3a;
    --muted: #8a8a8a;
    --rule: #c9c9c9;
  }
  * { box-sizing: border-box; margin: 0; padding: 0; }
  html, body { width: 1200px; height: 871px; overflow: hidden; }
  body {
    background: var(--stage);
    font-family: "Roboto", Arial, sans-serif;
    position: relative;
  }
  .card {
    position: absolute;
    width: 640px;
    height: 366px;
    border-radius: 3px;
  }
  .card--front {
    left: 80px; top: 40px;
    background: linear-gradient(135deg, var(--maroon) 0%, var(--maroon-deep) 100%);
    display: flex; align-items: center; justify-content: center;
  }
  .card--back {
    left: 480px; top: 465px;
    background: var(--paper);
    border-bottom: 6px solid var(--maroon);
    color: var(--ink);
  }
  .wordmark {
    font-family: "Roboto", Arial, sans-serif;
    font-weight: 900;
    text-transform: uppercase;
    line-height: 1;
    text-align: center;
  }
  .card--front .wordmark { color: var(--paper); font-size: 40px; letter-spacing: 2px; }
  .card--front .wordmark span { display: block; }
  .back-logo {
    position: absolute; left: 34px; top: 38px;
    text-align: left;
  }
  .back-logo .wordmark { color: var(--maroon); font-size: 26px; text-align: left; letter-spacing: 1px; }
  .back-logo .tagline {
    margin-top: 6px; font-size: 10px; letter-spacing: 2px;
    color: var(--ink); text-transform: uppercase;
  }
  .rule {
    position: absolute; left: 34px; right: 34px; top: 200px;
    height: 1px; background: var(--rule);
  }
  .person { position: absolute; left: 34px; top: 212px; }
  .person__name {
    font-family: "Roboto Slab", Georgia, serif;
    font-weight: 700; font-size: 25px; color: var(--maroon);
    text-transform: uppercase;
  }
  .person__title { font-style: italic; font-size: 12px; color: var(--muted); margin-top: 3px; }
  .address {
    position: absolute; right: 34px; top: 150px;
    text-align: right; font-size: 12px; line-height: 1.5; color: var(--muted);
  }
  .website {
    position: absolute; right: 34px; top: 238px;
    font-family: "Roboto Slab", Georgia, serif;
    font-weight: 700; font-size: 13px; color: var(--ink);
  }
  .contacts { position: absolute; left: 34px; top: 282px; list-style: none; }
  .contacts li {
    display: flex; align-items: center; gap: 10px;
    font-size: 12px; color: var(--muted); line-height: 22px;
  }
  .contacts svg { width: 12px; height: 12px; fill: var(--maroon); }
</style>
</head>
<body>
  <section class="card card--front" aria-label="Business card front">
    <div class="wordmark"><span>Fendrow</span><span>Trade Builders</span></div>
  </section>

  <section class="card card--back" aria-label="Business card back">
    <div class="back-logo">
      <div class="wordmark">Fendrow Trade Builders</div>
      <div class="tagline">Development &amp; Construction</div>
    </div>

    <div class="address">24731 Harlowe<br>Rd Pinehollow, Tx 77590</div>
    <div class="rule"></div>

    <div class="person">
      <div class="person__name">Marcus L. Fendrow</div>
      <div class="person__title">President/CEO</div>
    </div>

    <div class="website">www.tbpbuildinggroup.net</div>

    <ul class="contacts">
      <li>
        <svg viewBox="0 0 24 24" aria-hidden="true"><path d="M6.6 10.8a15 15 0 0 0 6.6 6.6l2.2-2.2c.3-.3.7-.4 1-.2 1.1.4 2.3.6 3.6.6.6 0 1 .4 1 1V20c0 .6-.4 1-1 1C10.6 21 3 13.4 3 4c0-.6.4-1 1-1h3.5c.6 0 1 .4 1 1 0 1.3.2 2.5.6 3.6.1.3 0 .7-.2 1z"/></svg>
        281-555-0147
      </li>
      <li>
        <svg viewBox="0 0 24 24" aria-hidden="true"><path d="M7 1h10a2 2 0 0 1 2 2v18a2 2 0 0 1-2 2H7a2 2 0 0 1-2-2V3a2 2 0 0 1 2-2zm0 3v14h10V4zm5 15.5a1 1 0 1 0 0 2 1 1 0 0 0 0-2z"/></svg>
        281-555-0192
      </li>
      <li>
        <svg viewBox="0 0 24 24" aria-hidden="true"><path d="M2 5h20v14H2zm2 2v.5l8 5 8-5V7zm0 2.8V17h16V9.8l-8 5z"/></svg>
        mfendrow@tbpgrp.net
      </li>
    </ul>
  </section>
</body>
</html>
```